Voyage and Sail Halvora 2017

I need cover design and catalog/brochure layout for a deluxe trip.
The itinerary pages my contain 3 columns with information on the trip and color images ( column1 photo/ column2 destination description/column 3photo)
The graphic layout is most important and it needs to be in a double sided catalog format.
the project needs to use a common publishing software that can be imported into Microsoft Word or Apple Pages - this will allow me to enter the content

Target Market(s)

upscale travelers

Industry/Entity Type

Travel

Font styles to use
Serif

Requirements
Must have
• -very classy look and feel that appeals to experienced travelers 40 and older
• - layout that can be imported as a template in MS Word or Apple Pages
Nice to have
• Major improvement in layout and graphic design
Should not have
• project must not look like it was done by me! - professional appearance is paramount

```html
<!DOCTYPE html>
<html lang="en">
<head>
<meta charset="utf-8">
<title>Voyage and Sail Halvora 2017 – Itinerary Days 3 and 4</title>
<link rel="stylesheet" href="https://fonts.googleapis.com/css2?family=EB+Garamond:wght@400;500;600&display=swap">
<style>
  :root {
    --paper-top: #fdeecb;
    --paper-bottom: #fcf4e3;
    --ink: #333333;
    --ink-soft: #3d3d3d;
    --sky: #9fb4c8;
    --palace-gold: #c9a24a;
    --garden-green: #5e9a3e;
    --garden-pink: #d86a8a;
    --stone: #cbbfa4;
    --stone-sky: #4f7fbf;
    --library-wood: #5a3f22;
    --library-gold: #b08a3e;
  }
  * { margin: 0; padding: 0; box-sizing: border-box; }
  html, body { width: 848px; height: 1200px; overflow: hidden; }
  body { background: var(--paper-bottom); }
  .page {
    position: relative;
    width: 848px;
    height: 1200px;
    background: linear-gradient(180deg, var(--paper-top) 0%, var(--paper-bottom) 100%);
    color: var(--ink);
    font-family: "EB Garamond", serif;
    overflow: hidden;
  }
  .day {
    position: absolute;
    left: 36px;
    width: 776px;
    height: 540px;
    display: grid;
    grid-template-columns: 220px 1fr 220px;
    column-gap: 26px;
  }
  .day-3 { top: 50px; }
  .day-4 { top: 620px; }
  .day-info { padding-top: 2px; }
  .day-title {
    font-weight: 500;
    font-size: 31px;
    line-height: 36px;
    letter-spacing: -0.3px;
  }
  .day-route {
    font-weight: 600;
    font-size: 18.5px;
    line-height: 23px;
    margin-top: 12px;
  }
  .day-text {
    font-size: 16.5px;
    line-height: 23px;
    text-align: justify;
    hyphens: auto;
    color: var(--ink-soft);
    margin-top: 12px;
  }
  .photo { width: 220px; height: 300px; }
  .photo-lead { align-self: start; }
  .photo-close { align-self: end; }
  .photo-pena {
    background: linear-gradient(180deg, var(--sky) 0%, #8aa0b8 30%, var(--palace-gold) 58%, #2f4a2a 100%);
  }
  .photo-garden {
    background: linear-gradient(160deg, #dfe6d2 0%, var(--garden-green) 40%, var(--garden-pink) 70%, #3f6f2e 100%);
  }
  .photo-batalha {
    background: linear-gradient(180deg, var(--stone-sky) 0%, #a9bedb 28%, var(--stone) 60%, #a99a7c 100%);
  }
  .photo-library {
    background: linear-gradient(180deg, #3a2a18 0%, var(--library-wood) 35%, var(--library-gold) 62%, #8f8a80 100%);
  }
</style>
</head>
<body>
<main class="page">
  <section class="day day-3">
    <div class="photo photo-lead photo-pena" role="img" aria-label="Colourful hilltop palace with yellow and red towers above a forested valley"></div>
    <div class="day-info">
      <h2 class="day-title">Day 3</h2>
      <h3 class="day-route">Lisbon, Sintra, Pena Palace<br>Fishermans, Tavern, Luncheon,<br>Cascais, Old Town, Citadel, Estoril</h3>
      <p class="day-text">Meet your private chauffeur at the lobby Drive to Sintra, an extraordinary town with a surreal mixture of history and fantasy, Enjoy a private guided tour to Sintra historical centre with private visit to Pena Palace Drive continues towards Cascais, and neighboring Estoril,quaint fishing villages that were favored by 20th century European nobility.Today it is a colorful cosmopolitan town with elegant pedestrian streets, chic shops,restaurants and bars Lunch will be served at an old fishermen's tavern Leisure time in Cascais and Estoril, Drop-off at your hotel.</p>
    </div>
    <div class="photo photo-close photo-garden" role="img" aria-label="Lush palace garden path with palms and pink flowers"></div>
  </section>

  <section class="day day-4">
    <div class="photo photo-lead photo-batalha" role="img" aria-label="Gothic stone monastery under a blue sky"></div>
    <div class="day-info">
      <h2 class="day-title">Day 4</h2>
      <h3 class="day-route">Lisbon, Batalha Monestary,<br>Coimbra University Joanina<br>Library, Monetary ofSanta Cruz,<br>Cathedral ofCoimbra, Porto</h3>
      <p class="day-text">Meet your private chauffeur at the lobby Drive to Sintra, an extraordinary town with a surreal mixture of history and fantasy, Enjoy a private guided tour to Sintra historical centre with private visitto Pena Palace Drive continues towards Cascais, and neighboring Estoril, quaint fishing villages that were favored by 20th century European nobility. Today it is a colorful cosmopolitan town with elegant pedestrian streets, chic shops, restaurants and bars Lunch will be served at an old fishermen's tavern Leisure time in Cascais and Estoril, Drop-off at your hotel</p>
    </div>
    <div class="photo photo-close photo-library" role="img" aria-label="Ornate baroque library hall with gilded wooden bookcases"></div>
  </section>
</main>
</body>
</html>
```